Silver Lantern Pathways PowerPoint

Please edit the following attached PowerPoint entitled workshop. Use the other attached PDF "Brightvale Northern California Value Proposition" as a reference for the design and color I would like.

```html
<!DOCTYPE html>
<html lang="en">
<head>
<meta charset="utf-8">
<title>Silver Lantern Pathways – Workshop</title>
<link href="https://fonts.googleapis.com/css2?family=Poppins:wght@400;500;600;700;800&display=swap" rel="stylesheet">
<style>
:root{
  --navy:#0b2d6f;
  --navy-deep:#082560;
  --sky:#9ccfee;
  --sky-text:#8cc2ec;
  --tint:#eaf3fa;
  --page:#e8e8e8;
  --ink:#111;
  --white:#fff;
}
*{box-sizing:border-box;margin:0;padding:0}
html,body{width:1200px;height:3456px;overflow:hidden}
body{background:var(--page);font-family:'Poppins',sans-serif;color:var(--ink);position:relative}
.slide{position:absolute;left:50px;width:1099px;height:620px;background:var(--white);overflow:hidden;box-shadow:0 2px 3px rgba(0,0,0,.12)}
.slide-header{position:absolute;left:0;top:0;width:100%;height:106px;background:var(--navy)}
.slide-header::before{content:"";position:absolute;left:0;top:0;width:122px;height:7px;background:var(--sky)}
.slide-header::after{content:"";position:absolute;right:0;bottom:0;width:122px;height:7px;background:var(--sky)}
.slide-title{position:absolute;left:55px;top:28px;font-weight:800;font-size:35px;color:var(--white);letter-spacing:.2px;white-space:nowrap}
.slide-title .accent{color:var(--sky-text)}

/* Slide 1 */
.intro{top:67px;background:var(--navy)}
.intro-title{position:absolute;left:55px;top:48px;font-size:43px;font-weight:800;color:var(--white)}
.intro-card{position:absolute;left:55px;width:640px;border-radius:22px 0 0 22px;padding:28px 22px;font-size:20px;color:var(--navy);line-height:1.25;background:linear-gradient(90deg,#fff 0%,rgba(255,255,255,.75) 40%,rgba(255,255,255,0) 95%)}
.intro-card b{font-weight:700}
.intro-card ul{list-style:none}
.intro-card li::before{content:"• "}
.card-objective{top:129px;height:121px}
.card-how{top:270px;height:123px;padding-top:16px}
.card-key{top:412px;height:122px;background:linear-gradient(90deg,#a9d6f2 0%,rgba(120,180,230,.6) 45%,rgba(80,130,200,0) 95%);color:var(--white);font-weight:800;font-size:26px;line-height:1.3;padding-top:25px}
.intro-photo{position:absolute;left:621px;top:80px;width:478px;height:486px;border-radius:243px 0 0 243px;background:radial-gradient(circle at 60% 55%,#d9c7a4 0%,#b79f78 22%,#8fae5a 45%,#5f8f2e 75%,#3f6a1f 100%)}

/* Slide 2 */
.importance{top:740px}
.lead{position:absolute;left:0;width:100%;text-align:center;font-size:23px;line-height:1.2}
.loss-card{position:absolute;top:322px;width:129px;height:242px;background:var(--white);border-radius:8px;box-shadow:0 3px 8px rgba(0,0,0,.12);overflow:hidden;text-align:center}
.loss-icon{height:86px;display:flex;align-items:center;justify-content:center}
.loss-icon.dark{background:var(--navy)}
.loss-icon.light{background:var(--sky)}
.loss-icon svg{width:44px;height:44px;fill:none;stroke:#fff;stroke-width:2;stroke-linecap:round;stroke-linejoin:round}
.loss-icon.light svg{stroke:var(--navy)}
.loss-label{padding-top:34px;font-size:18px;line-height:1.2}

/* Slide 3 */
.efficiency{top:1413px}
.compare{position:absolute;top:146px;width:481px;height:424px;border-radius:22px;text-align:center;font-size:27px;line-height:1.22;padding-top:72px}
.compare::before,.compare::after{content:"";position:absolute;left:50%;width:64px;height:2px;margin-left:-32px}
.compare::before{top:46px}
.compare::after{bottom:40px}
.compare-inefficient{left:55px;background:var(--navy);color:var(--white)}
.compare-inefficient::before,.compare-inefficient::after{background:var(--white)}
.compare-efficient{left:563px;background:var(--sky);color:var(--navy-deep)}
.compare-efficient::before,.compare-efficient::after{background:var(--navy)}
.big{font-size:43px;font-weight:700;line-height:1.15}
.big span{font-weight:400}

/* Slide 4 */
.distribution{top:2087px}
.distribution-tint{position:absolute;left:0;top:310px;width:100%;height:310px;background:var(--tint)}
.illustration-card{position:absolute;left:55px;top:134px;width:990px;height:372px;background:var(--white);border-radius:16px;box-shadow:0 2px 8px rgba(0,0,0,.08)}
.illustration{position:absolute;left:117px;top:40px;width:712px;height:300px;background:linear-gradient(180deg,#f6f7f5,#e3e8e3)}
.question{position:absolute;left:154px;top:523px;display:flex;align-items:center;gap:26px;font-size:27px;line-height:1.15;color:var(--ink)}
.question svg{width:88px;height:64px;fill:none;stroke:var(--navy);stroke-width:3;stroke-linejoin:round}

/* Slide 5 */
.hierarchy{top:2760px}
.hierarchy .slide-title{top:10px}
.slide-subtitle{position:absolute;left:55px;top:62px;font-size:23px;font-weight:700;color:var(--sky-text)}
.col-label{position:absolute;top:140px;font-size:20px;font-weight:700;color:var(--navy)}
.pyramid{position:absolute;left:0;top:0;width:1099px;height:620px}
.tier-text{position:absolute;font-size:18px;line-height:1.25;color:var(--ink)}
.tier-text b{font-weight:700;font-size:19px}
.tier-text ul{list-style:none;font-size:17px}
.tier-text li::before{content:"• "}
.tier-text .small{font-size:17px}
</style>
</head>
<body>

<section class="slide intro">
  <h1 class="intro-title">YOUR MONEY</h1>
  <div class="intro-card card-objective"><b>Objective:</b><br>• Build as big as possible</div>
  <div class="intro-card card-how"><b>How:</b>
    <ul><li>Higher rates of return?</li><li>More risk?</li><li>“Better” products?</li></ul>
  </div>
  <div class="intro-card card-key">Having an efficient overall strategy<br>is the key; it all starts here!</div>
  <div class="intro-photo" role="img" aria-label="Photo of a burlap money bag with a dollar sign beside stacked coins on a green background"></div>
</section>

<section class="slide importance">
  <header class="slide-header"><h2 class="slide-title">WHY IS YOUR STRATEGY SO <span class="accent">IMPORTANT?</span></h2></header>
  <p class="lead" style="top:142px">We all only have a finite amount of money…<br>we have to be efficient with it in the short time we have.</p>
  <p class="lead" style="top:219px">Inefficiencies cause major losses to occur.</p>
  <p class="lead" style="top:284px">These losses can be reflected in:</p>

  <div class="loss-card" style="left:55px"><div class="loss-icon dark"><svg viewBox="0 0 44 44"><path d="M22 16c-2-4-8-3-8 1 0 4 8 9 8 9s8-5 8-9c0-4-6-5-8-1z"/><path d="M6 28l6 8h8M38 28l-6 8h-8"/></svg></div><div class="loss-label">Lower<br>current<br>lifestyle</div></div>
  <div class="loss-card" style="left:199px"><div class="loss-icon light"><svg viewBox="0 0 44 44"><circle cx="24" cy="12" r="7"/><path d="M24 8v8M6 30h8l6 3h10l8-6M6 36h10"/></svg></div><div class="loss-label">Lower<br>retirement<br>income</div></div>
  <div class="loss-card" style="left:342px"><div class="loss-icon dark"><svg viewBox="0 0 44 44"><path d="M22 6l12 5v9c0 8-6 13-12 16-6-3-12-8-12-16v-9z"/><path d="M16 21l4 4 8-8"/></svg></div><div class="loss-label">Inadequate<br>protection</div></div>
  <div class="loss-card" style="left:486px"><div class="loss-icon light"><svg viewBox="0 0 44 44"><path d="M10 6h16l6 6v26H10z"/><path d="M15 32v-4M20 32v-7M25 32v-5"/><circle cx="30" cy="18" r="5"/></svg></div><div class="loss-label">Loss of<br>financial<br>control</div></div>
  <div class="loss-card" style="left:630px"><div class="loss-icon dark"><svg viewBox="0 0 44 44"><circle cx="22" cy="16" r="7"/><path d="M22 12v8M8 32h8l6 3h10l6-5M30 8l6-2v6"/></svg></div><div class="loss-label">Financial<br>vulnerability</div></div>
  <div class="loss-card" style="left:773px"><div class="loss-icon light"><svg viewBox="0 0 44 44"><path d="M10 8h24v28H10z"/><path d="M14 14h16M14 34h16"/><circle cx="27" cy="24" r="4"/><path d="M14 28l6-8"/></svg></div><div class="loss-label">Higher taxes<br>and fees</div></div>
  <div class="loss-card" style="left:917px"><div class="loss-icon dark"><svg viewBox="0 0 44 44"><path d="M8 36h28M12 36v-8M18 36v-12M24 36v-6M30 36v-14"/><circle cx="20" cy="12" r="4"/></svg></div><div class="loss-label">Less<br>benefits</div></div>
</section>

<section class="slide efficiency">
  <header class="slide-header"><h2 class="slide-title">HOW SIGNIFICANT IS <span class="accent">EFFICIENCY?</span></h2></header>
  <div class="compare compare-inefficient">An individual might be<br>able to create<br><span class="big">$75,000<span>/year</span></span><br>(1 unit)<br>of retirement income based<br>on current savings<br>with an inefficient process.</div>
  <div class="compare compare-efficient">The same individual<br>could create<br><span class="big">$125,000<span>/year</span></span><br>of retirement income<br>with an efficient process<br>using the same amount<br>of savings.</div>
</section>

<section class="slide distribution">
  <header class="slide-header"><h2 class="slide-title">DISTRIBUTION RATES</h2></header>
  <div class="distribution-tint"></div>
  <div class="illustration-card">
    <div class="illustration" role="img" aria-label="Sketch illustration of savings piles on two mountains, one paying out a $1,000,000 sum and the other a steady $70,000–$130,000 a year income"></div>
  </div>
  <div class="question">
    <svg viewBox="0 0 88 64"><path d="M4 4h50v32H24l-10 10v-10H4z"/><path d="M58 20h26v28h-8v8l-8-8H34v-8"/><path d="M23 14c0-6 12-6 12 0 0 4-6 4-6 9M29 28v1"/></svg>
    <span>How could you do this without higher probabilities<br>of running out of money?</span>
  </div>
</section>

<section class="slide hierarchy">
  <header class="slide-header">
    <h2 class="slide-title">RETIREMENT INCOME STRATEGY HIERARCHY</h2>
    <p class="slide-subtitle">(Highest to Lowest Efficiency)</p>
  </header>
  <p class="col-label" style="left:195px">Retirement Income Strategies</p>
  <p class="col-label" style="left:957px">Efficiency</p>

  <svg class="pyramid" viewBox="0 0 819 462" aria-hidden="true">
    <defs>
      <linearGradient id="arrowFill" x1="0" y1="0" x2="0" y2="1">
        <stop offset="0" stop-color="#a9d6f2"/><stop offset="1" stop-color="#0b2d6f"/>
      </linearGradient>
    </defs>
    <polygon points="263,136 312,202 214,202" fill="#0b2d6f"/>
    <polygon points="209,208 317,208 369,277 158,277" fill="#9ccfee"/>
    <polygon points="153,283 373,283 424,351 102,351" fill="#0b2d6f"/>
    <polygon points="98,357 428,357 480,426 46,426" fill="#9ccfee"/>
    <g fill="#fff"><circle cx="263" cy="178" r="11"/><circle cx="263" cy="245" r="11"/><circle cx="263" cy="319" r="11"/><circle cx="263" cy="389" r="11"/></g>
    <g fill="#0b2d6f" font-family="Poppins,sans-serif" font-weight="700" font-size="14" text-anchor="middle">
      <text x="263" y="183">1</text><text x="263" y="250">2</text><text x="263" y="324">3</text><text x="263" y="394">4</text>
    </g>
    <g stroke="#777" stroke-width="0.8">
      <line x1="328" y1="205" x2="722" y2="205"/>
      <line x1="380" y1="280" x2="722" y2="280"/>
      <line x1="430" y1="354" x2="722" y2="354"/>
    </g>
    <polygon points="753,129 775,150 765,150 765,426 741,426 741,150 731,150" fill="url(#arrowFill)"/>
  </svg>

  <div class="tier-text" style="left:441px;top:192px"><b>Twin Income Engines Approach:</b>
    <ul><li>Covered Assets Option (Guaranteed*)</li><li>Volatility Buffer Option (Non-Guaranteed)</li></ul>
  </div>
  <div class="tier-text" style="left:518px;top:310px">Joint Single Premium Immediate<br>Annuity (Guaranteed*)</div>
  <div class="tier-text" style="left:581px;top:408px">Growth Annuity with Income Rider<br>(Guaranteed*)</div>
  <div class="tier-text" style="left:643px;top:490px"><b>Single Income Engine Approach:</b><br><span class="small">Investments Only using Withdrawal Rate<br>Simulations (Non-Guaranteed)</span></div>
</section>

</body>
</html>
```